Private label Bottled water label design

We are launching private label water bottle case packs with our brand “tallybrook”
Need bottle labels design as well as case pack design artwork. Bottle is 16.9oz similar to pet quarvin plimsey bottles.
It will be spring water.
Case pack will be of 24 bottles
Tallybrook is a chain of convenience stores in Texas
www.tallybrookmarts.example
I have attached pictures of quarvin water. It would be similar packaging for single and case pack.

Target Market(s)

Male female shoppers middle aged. Take home package or single serve in cold vault

Industry/Entity Type

Water bottle retail

Colors
0054AA
0677BA
7BADD7
CADEEF
E8F1F8
59FF00
82FF00
B8FF75
E3FFCB
F4FFEA

Requirements
Must have
• Very premium look. Use the logo of tallybrook
Nice to have
• Elegant premium water look
Should not have
• I am open to all

```html
<!DOCTYPE html>
<html lang="en">
<head>
<meta charset="UTF-8">
<title>Tallybrook Spring Water – Bottle Label</title>
<link rel="stylesheet" href="https://fonts.googleapis.com/css2?family=Lilita+One&family=Nunito:wght@800&display=swap">
<style>
  :root {
    --page-bg: #e8f1f8;
    --forest-deep: #1c4a4f;
    --forest-mid: #2e7370;
    --forest-light: #5d9a86;
    --sky: #a9d0de;
    --water-deep: #1f5f7a;
    --water-light: #4f97b3;
    --brand-blue: #0054aa;
    --brand-blue-mid: #0677ba;
    --white: #ffffff;
    --seal: #cadeef;
    --accent-green: #82ff00;
  }
  * { margin: 0; padding: 0; box-sizing: border-box; }
  html, body {
    width: 1200px;
    height: 900px;
    overflow: hidden;
    background: var(--page-bg);
  }
  .canvas {
    position: relative;
    width: 1200px;
    height: 900px;
    display: flex;
    align-items: center;
    justify-content: center;
  }
  .bottle-label {
    position: relative;
    width: 1000px;
    height: 640px;
    border-radius: 10px;
    overflow: hidden;
    box-shadow: 0 10px 30px rgba(0, 84, 170, 0.18);
  }
  .label-scenery {
    position: absolute;
    inset: 0;
    background:
      radial-gradient(ellipse 40% 30% at 55% 22%, var(--sky) 0%, rgba(169,208,222,0) 100%),
      linear-gradient(180deg,
        var(--forest-deep) 0%,
        var(--forest-mid) 30%,
        var(--forest-light) 52%,
        var(--water-light) 72%,
        var(--water-deep) 100%);
  }
  .brand-lockup {
    position: absolute;
    top: 150px;
    left: 0;
    right: 0;
    display: flex;
    align-items: center;
    justify-content: center;
    gap: 18px;
  }
  .brand-dot {
    width: 34px;
    height: 34px;
    border-radius: 50%;
    background: var(--white);
  }
  .brand-name {
    font-family: "Nunito", sans-serif;
    font-weight: 800;
    font-size: 118px;
    line-height: 1;
    color: var(--white);
    letter-spacing: -2px;
  }
  .product-name {
    position: absolute;
    top: 310px;
    left: 0;
    right: 0;
    text-align: center;
    font-family: "Lilita One", sans-serif;
    font-size: 140px;
    line-height: 1;
    color: var(--brand-blue-mid);
    -webkit-text-stroke: 6px var(--white);
    paint-order: stroke fill;
    letter-spacing: 1px;
  }
  .volume {
    position: absolute;
    top: 468px;
    left: 0;
    right: 0;
    text-align: center;
    font-family: "Nunito", sans-serif;
    font-weight: 800;
    font-size: 34px;
    color: var(--white);
  }
  .quality-seal {
    position: absolute;
    top: 90px;
    right: 24px;
    width: 110px;
    height: 110px;
  }
</style>
</head>
<body>
  <main class="canvas">
    <section class="bottle-label">
      <div class="label-scenery" role="img" aria-label="Illustrated forest spring with trees, sky and flowing water with a splashing droplet"></div>

      <div class="brand-lockup">
        <span class="brand-name">tallybrook</span>
        <span class="brand-dot"></span>
      </div>

      <h1 class="product-name">SPRING WATER</h1>
      <p class="volume">16oz/0.5L</p>

      <svg class="quality-seal" viewBox="0 0 110 110" role="img" aria-label="Quality seal">
        <circle cx="55" cy="55" r="50" fill="var(--seal)" fill-opacity="0.55" stroke="var(--white)" stroke-width="3"/>
      </svg>
    </section>
  </main>
</body>
</html>
```